Black Granite Web Design Project

We are looking for a design for a new company that will be selling Black Granite slabs and tiles. We will be selling to both end-consumers and granite installers. We have already settled on a logo and hopefully this will give an idea of what we like in our designs. We are not going to be selling online but want people to call us so the site is basically an enhanced business card. We will be focusing a lot on SEO so the design will have to keep that in mind.

We would like to keep the design in 1024x768 to make it easily view-able on all devices.

Regarding navigation there should only be a few sub-pages, like "Granite Slabs", "Granite Tiles", "Delivery", "Contact"

Aside from that we are open to designs. One idea we did have was to personalize the site and have a person there somehow to represent the company, making the user feel there are real people behind this site. This is just an idea and not a must.

The name of the company and site is "Silver Brook Petrano"

Thanks
Updates

Hello All,

Thanks for the great designs. There are some good looking designs that show beautiful kitchens but this site is made for the granite installers and not the retail consumers. So in order not to to confuse the buyers I would like to keep this as much about the raw products as possible. The raw products being the granite slabs, thereby making it obvious we don't sell granite counter tops. 

This design will really be the identity of this company so it is important we get the right message across on this index page and that this page is as complete as possible.

Again, thanks for all the work being put into this.

Target Market(s)

The target audience is granite installers or companies that would with granite slabs.

Industry/Entity Type

Business

```html
<!DOCTYPE html>
<html lang="en">
<head>
<meta charset="utf-8">
<title>Silver Brook Petrano</title>
<link href="https://fonts.googleapis.com/css2?family=Oswald:wght@400;500;700&family=PT+Sans:wght@400;700&display=swap" rel="stylesheet">
<style>
:root{
  --ink:#1a1a1a;
  --hero-dark:#252628;
  --green:#9dc63a;
  --green-deep:#5b7d32;
  --card-black:#000;
  --text:#333;
  --muted:#777;
  --footer:#2d2e30;
  --footer-line:#555759;
  --white:#fff;
}
*{margin:0;padding:0;box-sizing:border-box}
html,body{width:1099px;height:1200px;overflow:hidden;background:#fff}
body{position:relative;font-family:"PT Sans",sans-serif;color:var(--text)}
.abs{position:absolute}

/* header */
.brand{left:56px;top:34px;display:flex;align-items:center;gap:12px}
.brand-mark{width:54px;height:54px;background:var(--ink)}
.brand-name{font-family:"Oswald",sans-serif;font-weight:700;font-size:28px;line-height:1;color:var(--ink);text-transform:uppercase;letter-spacing:-.3px}
.brand-place{font-family:"PT Sans",sans-serif;font-size:12px;letter-spacing:2px;color:var(--ink);margin-top:3px;text-transform:uppercase}
.social{left:894px;top:16px;display:flex;gap:11px}
.social span{width:27px;height:27px;border-radius:3px;background:#8a8c8f}
.nav{right:62px;top:68px;display:flex;font-family:"Oswald",sans-serif;font-weight:500;font-size:17px;color:var(--ink);text-transform:uppercase}
.nav a{color:inherit;text-decoration:none;padding:0 13px;border-left:1px solid #ccc;line-height:20px}
.nav a:first-child{border-left:0}
.nav a:last-child{padding-right:0}

/* hero */
.hero{left:0;top:117px;width:1099px;height:440px;background:var(--hero-dark)}
.hero-photo{left:447px;top:117px;width:652px;height:440px;background:linear-gradient(90deg,var(--hero-dark) 0%,#2f3030 12%,#2a2b2b 60%,#5a5b58 85%,#b8b8b2 100%)}
.hero-kicker{left:78px;top:208px;font-family:"Oswald",sans-serif;font-weight:700;font-size:38px;line-height:1;color:var(--green-deep)}
.hero-title{left:78px;top:252px;font-family:"Oswald",sans-serif;font-weight:700;font-size:43px;line-height:1;color:var(--white)}
.hero-text{left:81px;top:302px;width:380px;font-size:14px;line-height:21px;color:#e8e8e8}
.btn{left:82px;top:378px;width:106px;height:35px;background:linear-gradient(#6c9a3a,#4b7426);color:var(--white);font-family:"Oswald",sans-serif;font-size:15px;text-align:center;line-height:35px;border:1px solid #7eb04a}
.arrows{left:86px;top:436px}

/* cards */
.card{top:527px;width:313px;height:226px}
.card-img{width:313px;height:153px;border:1px solid #ddd}
.card-cap{height:73px;background:var(--card-black);padding:12px 19px}
.card-cap h3{font-family:"Oswald",sans-serif;font-weight:700;font-size:22px;line-height:26px;color:var(--green);text-transform:uppercase}
.card-cap p{font-family:"Oswald",sans-serif;font-size:13px;line-height:20px;color:#e6e6e6;text-transform:uppercase}

/* content */
.welcome{left:55px;top:806px;width:650px}
.welcome h2,.quality h2{font-weight:400;font-size:27px;color:#222;margin-bottom:12px;line-height:34px}
.welcome p{font-size:13px;line-height:21.5px;color:#3a3a3a;margin-bottom:15px}
.quality{left:733px;top:808px;width:330px}
.quality-body{display:flex;gap:12px}
.quality-img{width:110px;height:115px;flex:none;border-radius:3px;background:linear-gradient(160deg,#6d8fb3,#2b3440 55%,#a46c4b)}
.quality h4{font-weight:400;font-size:18px;color:#222;line-height:22px;margin-top:-2px}
.quality p{font-size:13px;line-height:22px;color:var(--muted)}

/* footer */
.footer{left:0;top:1054px;width:1099px;height:146px;background:var(--footer);border-top:5px solid var(--footer-line)}
.foot-nav{left:58px;top:1093px;font-size:16px;color:#ddd}
.foot-nav span{padding:0 5px;color:#aaa}
.copy{left:58px;top:1128px;font-size:13px;color:#bbb}
.foot-brand{left:840px;top:1126px;width:178px;text-align:center;color:var(--white)}
.foot-brand .brand-name{color:var(--white);font-size:22px}
.foot-brand .brand-place{color:#ccc;font-size:9px;letter-spacing:2px}
</style>
</head>
<body>

<header>
  <div class="abs brand">
    <div class="brand-mark"></div>
    <div>
      <div class="brand-name">Silver Brook Petrano</div>
      <div class="brand-place">Vale Claro</div>
    </div>
  </div>
  <div class="abs social"><span></span><span></span><span></span><span></span></div>
  <nav class="abs nav">
    <a href="#">Home</a><a href="#">Granit Slabs</a><a href="#">Granite Tiles</a><a href="#">Delivery</a><a href="#">Contact</a>
  </nav>
</header>

<section>
  <div class="abs hero"></div>
  <div class="abs hero-photo" role="img" aria-label="Polished black granite slab standing in a warehouse"></div>
  <div class="abs hero-kicker">WE SELL BEST</div>
  <h1 class="abs hero-title">BLACK GRANITE SLABS</h1>
  <p class="abs hero-text">Maecenas aliquet velit vel turpis. Mauris neque metus, malesuada nec, ultricies sit amet, porttitor mattis, enim. In massa libero, interdum nec, interdum vel, blandit sed, nulla.</p>
  <a class="abs btn">ORDER NOW</a>
  <svg class="abs arrows" width="36" height="24" viewBox="0 0 36 24"><path d="M12 2 3 12l9 10M24 2l9 10-9 10" fill="none" stroke="#fff" stroke-width="2"/></svg>
</section>

<section>
  <div class="abs card" style="left:52px">
    <div class="card-img" role="img" aria-label="Granite slabs in a stone yard" style="background:linear-gradient(135deg,#3a3d40,#6a6d6f 60%,#a8a9a5)"></div>
    <div class="card-cap"><h3>Granit Slabs</h3><p>Maecenas aliquet velit vel turpis mauris nequ</p></div>
  </div>
  <div class="abs card" style="left:390px">
    <div class="card-img" role="img" aria-label="Bathroom floor laid with black granite tiles" style="background:linear-gradient(160deg,#8e9092,#2a2c2e 55%,#111)"></div>
    <div class="card-cap"><h3>Granit Tiles</h3><p>Maecenas aliquet velit vel turpis nequ</p></div>
  </div>
  <div class="abs card" style="left:727px">
    <div class="card-img" role="img" aria-label="Large black granite slab ready for order" style="background:linear-gradient(135deg,#7c8a90,#1f2628 45%,#2b3234 70%,#9aa3a5)"></div>
    <div class="card-cap"><h3>Ordre Now</h3><p>Maecenas aliquet velit vel turpis mauris nequ</p></div>
  </div>
</section>

<section class="abs welcome">
  <h2>Welcome to Our Website Mainpage</h2>
  <p>Phasellus felis dolor, scelerisque a, tempus eget, lobortis id, libero. Donec scelerisque leo ac risus. Praesent sit amet est. In dictum, dolor eu dictum porttitor, enim felis viverra mi, eget luctus massa purus quis odio. Etiam nulla massa, pharetra facilisis, volutpat in, imperdiet sit amet, sem.</p>
  <p>Maecenas aliquet velit vel turpis. Mauris neque metus, malesuada nec, ultricies sit amet, porttitor mattis, enim. In massa libero, interdum nec, interdum vel, blandit sed, nulla. In ullamcorper, est eget tempor cursus, neque mi consectetuer mi, a ultricies massa est sed nisl.</p>
</section>

<aside class="abs quality">
  <h2>Quality &amp; Delivery</h2>
  <div class="quality-body">
    <div class="quality-img" role="img" aria-label="Granite slab loaded for outdoor delivery"></div>
    <div>
      <h4>Massa libero interdum</h4>
      <p>Interdum vel, blandit sed, nulla. In ullamcorper, est eget tempor cursus, neque mi consectetuer mi, a ultricies massa.</p>
    </div>
  </div>
</aside>

<footer>
  <div class="abs footer"></div>
  <div class="abs foot-nav">Home<span>|</span>Granit Slabs<span>|</span>Granite Tiles<span>|</span>Delivery<span>|</span>Contact</div>
  <div class="abs copy">© 2013 Company Name.&nbsp; All right reserved.&nbsp; Term of Use</div>
  <div class="abs foot-brand">
    <div class="brand-name">Silver Brook Petrano</div>
    <div class="brand-place">Vale Claro</div>
  </div>
</footer>

</body>
</html>
```